Classic and neutral book cover design

We are looking for a classic and neutral book cover design to be used as the template for a series of books to be published. We are hence looking for a template that will allow us to easily change the title name for all books in this series.
The use of very few colours (black and white is welcome) and few design elements is a big bonus. As a source of inspiration we would like to ask you to view the very simple and
If you think you have a cool idea that can add a twist to the formal classic look don't hesitate. Go for it !
Work will be done for a 30 year old Sweden based cultural non-profit called VĂ©lra (www.velrafoundation.example). We work with the publishing and supporting of post-modern art and literature addressing contemporary topics but are also involved in assisting projects of cultural preservation.
Target Market(s)
The audience is expected to have some form of interest in culture but could range from hobbyist readers to tenure track scholars
Industry/Entity Type
Non-Profit
Requirements
Must have
- General:
- Classic and neutral feel
- Preferably very simple and few shapes
- usage of few colours (black and white is welcome)
Information to be displayed on the cover is:
- Author
- Title
- type of work e.g. play/novel (optional)
- publishing house (in this case "Velra Publishing")
Nice to have
- ideas to prevent it from become boring are of course welcome
Should not have
- - too many colours

```html
<!DOCTYPE html>
<html lang="en">
<head>
<meta charset="utf-8">
<title>Book Title – Vélra Publishing</title>
<link rel="stylesheet" href="https://fonts.googleapis.com/css2?family=Berkshire+Swash&family=Raleway:wght@300;400;600&display=swap">
<style>
  :root {
    --ink: #4a1818;
    --frame: #9a6a4a;
    --wash-light: #fde6b0;
    --wash-mid: #f9c98a;
    --wash-warm: #f5b27a;
    --wash-rose: #f2ab92;
    --wash-pale: #fff3dc;
  }
  html, body {
    margin: 0;
    padding: 0;
    overflow: hidden;
    background: #ffffff;
  }
  .cover {
    position: relative;
    width: 848px;
    height: 1200px;
    overflow: hidden;
    font-family: "Raleway", sans-serif;
    color: var(--ink);
  }
  .cover__wash {
    position: absolute;
    inset: 0;
    background:
      radial-gradient(ellipse 300px 380px at 440px 640px, var(--wash-rose) 0%, rgba(242,171,146,0) 100%),
      radial-gradient(ellipse 260px 300px at 200px 300px, var(--wash-warm) 0%, rgba(245,178,122,0) 100%),
      radial-gradient(ellipse 280px 320px at 660px 900px, var(--wash-warm) 0%, rgba(245,178,122,0) 100%),
      radial-gradient(ellipse 200px 260px at 40px 450px, var(--wash-pale) 0%, rgba(255,243,220,0) 100%),
      radial-gradient(ellipse 220px 240px at 820px 1150px, var(--wash-pale) 0%, rgba(255,243,220,0) 100%),
      linear-gradient(160deg, var(--wash-light) 0%, var(--wash-mid) 45%, var(--wash-light) 100%);
  }
  .cover__frame {
    position: absolute;
    left: 64px;
    top: 80px;
    width: 710px;
    height: 1046px;
    border: 3px dotted var(--frame);
    overflow: hidden;
  }
  .cover__author {
    position: absolute;
    top: 142px;
    left: 0;
    width: 100%;
    text-align: center;
    font-weight: 400;
    font-size: 25px;
    letter-spacing: 0.5px;
    text-transform: uppercase;
  }
  .cover__title {
    position: absolute;
    top: 212px;
    left: 0;
    width: 100%;
    margin: 0;
    text-align: center;
    font-family: "Berkshire Swash", serif;
    font-weight: 400;
    font-size: 92px;
    line-height: 1.2;
  }
  .cover__genre {
    position: absolute;
    top: 366px;
    left: 122px;
    width: 596px;
    display: flex;
    align-items: center;
    gap: 14px;
    font-size: 24px;
    font-weight: 400;
  }
  .cover__genre::before,
  .cover__genre::after {
    content: "";
    flex: 1;
    height: 1px;
    background: var(--ink);
  }
  .cover__publisher {
    position: absolute;
    top: 918px;
    left: 0;
    width: 100%;
    text-align: center;
    font-weight: 600;
    font-size: 46px;
    text-transform: uppercase;
    letter-spacing: 1px;
  }
  .cover__publisher-echo {
    position: absolute;
    top: 950px;
    left: -64px;
    width: 848px;
    text-align: center;
    font-weight: 600;
    font-size: 150px;
    text-transform: uppercase;
    color: var(--ink);
    opacity: 0.07;
    line-height: 1;
  }
</style>
</head>
<body>
  <main class="cover">
    <div class="cover__wash" role="img" aria-label="Soft watercolour wash in warm yellow, orange and rose tones"></div>
    <div class="cover__frame">
      <div class="cover__publisher-echo" aria-hidden="true">Vélra</div>
    </div>
    <p class="cover__author">Author Name</p>
    <h1 class="cover__title">Book Title</h1>
    <p class="cover__genre" style="margin:0">roman</p>
    <p class="cover__publisher" style="margin:0">Vélra</p>
  </main>
</body>
</html>
```